BUSINESS CARD - HALVERDINE RURAL SERVICES

I would like to create a business card for my fertilizer spreading business. I would like to incorporate my existing logo and also a description of the services offered. The business card will be given to farmers so must be kept simple but effective. It will also be left in stores so much also be eye catching in order to stand out from other cards.

Target Market(s)

FARMERS

Requirements
Must have
• FRONT OF CARD = EXISTING LOGO + "CUSTOMISED SPREADING" below the logo

REAR Of CARD = SERVICES OFFERED AND CONTACT DETAILS

- Bulk fertilizer including Lime, Gypsum, Manure & Compost
- Granular fertilizer including Single Super, Urea, Grano-S, & Custom Blends
- Modern equipment - Autosteer & Variable Rate Capable
- Friendly & Reliable Service
- Contact Gus: 0471 502 318
Nice to have
• utilize same color scheme as existing logo

```html
<!DOCTYPE html>
<html lang="en">
<head>
<meta charset="utf-8">
<title>Halverdine Rural Services – Business Card</title>
<link rel="stylesheet" href="https://fonts.googleapis.com/css2?family=Exo+2:wght@600;700&family=Open+Sans:wght@400;600&display=swap">
<style>
  :root {
    --backdrop: #3d434a;
    --card: #ffffff;
    --orange: #f7a224;
    --orange-light: #fbd08f;
    --grey: #58595b;
    --text: #4a4a4a;
    --white: #ffffff;
  }
  * { margin: 0; padding: 0; box-sizing: border-box; }
  html, body {
    width: 1200px; height: 1200px; overflow: hidden;
    background: var(--backdrop);
  }
  .stage { position: relative; width: 1200px; height: 1200px; }

  .card {
    position: absolute; left: 186px; width: 840px; height: 479px;
    background: var(--card); overflow: hidden;
  }
  .card--front { top: 92px; }
  .card--back { top: 623px; }

  /* brand mark: plain circle + name */
  .brand { position: absolute; display: flex; flex-direction: column; align-items: center; }
  .brand__circle { border-radius: 50%; border: 8px solid var(--grey); }
  .brand__name {
    font-family: "Exo 2", sans-serif; font-weight: 700; color: var(--grey);
    white-space: nowrap; letter-spacing: -0.5px; line-height: 1.1;
  }
  .card--front .brand { left: 0; right: 0; top: 40px; }
  .card--front .brand__circle { width: 160px; height: 160px; }
  .card--front .brand__name { font-size: 40px; margin-top: 20px; }
  .card--back .brand { right: 30px; top: 14px; width: 190px; }
  .card--back .brand__circle { width: 78px; height: 78px; border-width: 5px; }
  .card--back .brand__name { font-size: 16px; margin-top: 8px; }

  .grass {
    position: absolute; left: 0; right: 0;
    background: linear-gradient(to bottom, rgba(247,162,36,0) 0%, var(--orange-light) 35%, var(--orange) 100%);
  }
  .card--front .grass { top: 286px; height: 124px; }
  .card--back .grass { top: 290px; height: 126px; }

  .band {
    position: absolute; left: 0; right: 0; bottom: 0;
    background: var(--orange);
    display: flex; align-items: center; justify-content: center;
    color: var(--white); font-family: "Exo 2", sans-serif; font-weight: 700;
    line-height: 1;
  }
  .card--front .band { height: 70px; font-size: 40px; letter-spacing: 1.5px; gap: 22px; }
  .band__rule { width: 88px; height: 2px; background: var(--white); }
  .card--back .band { height: 64px; font-size: 36px; gap: 14px; }

  .phone-icon { width: 34px; height: 34px; flex: none; }
  .phone-icon__disc { fill: var(--grey); }
  .phone-icon__handset { fill: var(--white); }

  .services { position: absolute; left: 24px; top: 52px; list-style: none; }
  .service { position: relative; padding-left: 44px; margin-bottom: 14px; }
  .service::before {
    content: ""; position: absolute; left: 4px; top: 8px;
    width: 18px; height: 12px; border-radius: 0 0 12px 12px; background: var(--orange);
  }
  .service__title {
    font-family: "Open Sans", sans-serif; font-weight: 600; font-size: 24px;
    color: var(--orange); line-height: 32px; text-transform: uppercase;
  }
  .service__detail {
    font-family: "Open Sans", sans-serif; font-weight: 400; font-size: 22px;
    color: var(--text); line-height: 32px;
  }
</style>
</head>
<body>
<main class="stage">
  <section class="card card--front" aria-label="Card front">
    <div class="brand">
      <div class="brand__circle"></div>
      <div class="brand__name">Halverdine Rural Services</div>
    </div>
    <div class="grass" role="img" aria-label="Orange grass silhouette along the bottom of the card"></div>
    <div class="band">
      <span class="band__rule"></span>
      <span>CUSTOMIZED SPREADING</span>
      <span class="band__rule"></span>
    </div>
  </section>

  <section class="card card--back" aria-label="Card back">
    <ul class="services">
      <li class="service">
        <div class="service__title">Bulk Fertilizer</div>
        <div class="service__detail">Lime, Gypsum, Manure &amp; Compost</div>
      </li>
      <li class="service">
        <div class="service__title">Granular Fertilizer</div>
        <div class="service__detail">Single Super, Urea, Grano-S, &amp; Custom Blends</div>
      </li>
      <li class="service">
        <div class="service__title">Modern Equipment</div>
        <div class="service__detail">Autosteer &amp; Variable Rate Capable</div>
      </li>
    </ul>
    <div class="brand">
      <div class="brand__circle"></div>
      <div class="brand__name">Halverdine Rural Services</div>
    </div>
    <div class="grass" role="img" aria-label="Orange grass silhouette along the bottom of the card"></div>
    <div class="band">
      <span>Call GUS</span>
      <svg class="phone-icon" viewBox="0 0 34 34" aria-hidden="true">
        <circle class="phone-icon__disc" cx="17" cy="17" r="17"/>
        <path class="phone-icon__handset" d="M11.5 9.5c.8-.8 1.9-.7 2.5.2l1.6 2.4c.5.8.4 1.8-.3 2.4l-1 .9c.9 2 2.4 3.5 4.3 4.4l.9-1c.6-.7 1.6-.8 2.4-.3l2.4 1.6c.9.6 1 1.7.2 2.5l-1.2 1.2c-1 1-2.6 1.3-4 .7-4.2-1.8-7.5-5.1-9.3-9.3-.6-1.4-.3-3 .7-4z"/>
      </svg>
      <span>0471 502 318</span>
    </div>
  </section>
</main>
</body>
</html>
```